Business Book - Building Calm Habits at the Office (Less Noise, More Focus Each Day)

I'm looking for a cover that appeals to successful business people who are used to reading business titles.

The cover should feel familiar and fit in with the existing canon of bestselling business books with a vibrant, but professional look (see attached).

I want my book to stand out, but not to be frivolous. Abstract is probably best. Or close to it.

Please feel free to use my brand colours, or go with something else -

Teal
HEX #199BAB
25 / 155 / 171

Coral
HEX #EE786E
238 / 120/ 110

I don't want to include anything connected with robots or gendered assistants/business people. Or headsets.

It's only 24 hours which is mental

```html
<!DOCTYPE html>
<html lang="en">
<head>
<meta charset="utf-8">
<title>Building Calm Habits at the Office — Book Cover</title>
<link href="https://fonts.googleapis.com/css2?family=Bebas+Neue&family=Questrial&display=swap" rel="stylesheet">
<style>
  :root {
    --teal: #209CAC;
    --coral: #EF786D;
    --slate: #6D6E71;
    --maroon: #652B26;
    --white: #FFFFFF;
    --ink: #111111;
  }
  html, body {
    margin: 0;
    padding: 0;
    width: 1200px;
    height: 1000px;
    overflow: hidden;
    background: var(--white);
  }
  .canvas {
    position: relative;
    display: block;
    width: 1200px;
    height: 1000px;
    margin: 0;
  }
  .cover-shapes {
    position: absolute;
    left: 0;
    top: 0;
  }
  .title {
    margin: 0;
    padding: 0;
    font-size: inherit;
    font-weight: inherit;
  }
  .kicker {
    position: absolute;
    left: 348px;
    width: 504px;
    top: 219px;
    margin: 0;
    text-align: center;
    font-family: "Questrial", sans-serif;
    font-size: 36px;
    letter-spacing: 1px;
    color: var(--white);
    line-height: 1;
    white-space: nowrap;
  }
  .headline {
    position: absolute;
    left: 348px;
    width: 504px;
    margin: 0;
    text-align: center;
    font-family: "Bebas Neue", sans-serif;
    font-weight: 400;
    font-size: 160px;
    line-height: 1;
    letter-spacing: 2px;
    color: var(--teal);
    white-space: nowrap;
    text-shadow:
      -6px 0 0 var(--white),
      -6px -2px 0 var(--white),
      -3px -2px 0 var(--white),
      0 -2px 0 var(--white),
      -6px 2px 0 var(--white),
      -3px 2px 0 var(--white),
      0 2px 0 var(--white),
      2px 0 0 var(--white);
  }
  .headline--first { top: 290px; }
  .headline--second { top: 472px; }
  .subtitle {
    position: absolute;
    left: 348px;
    width: 504px;
    top: 628px;
    margin: 0;
    text-align: center;
    font-family: "Questrial", sans-serif;
    font-size: 22px;
    color: var(--ink);
    line-height: 1;
    white-space: nowrap;
  }
</style>
</head>
<body>
  <main class="canvas">
    <svg class="cover-shapes" width="1200" height="1000" viewBox="0 0 1200 1000" aria-hidden="true">
      <rect class="cover-base" x="348" y="105" width="504" height="720" fill="var(--coral)"/>
      <polygon class="panel-teal" points="348,105 388,105 590,603 348,778" fill="var(--teal)"/>
      <polygon class="band-slate" points="428,718 590,603 610,615 505,743" fill="var(--slate)"/>
      <polygon class="corner-maroon" points="348,778 428,718 505,743 440,825 348,825" fill="var(--maroon)"/>
      <polygon class="wedge-white" points="610,615 852,752 852,825 772,825 505,743" fill="var(--white)"/>
    </svg>

    <h1 class="title">
      <span class="kicker">BUILDING CALM HABITS</span>
      <span class="headline headline--first">AT THE</span>
      <span class="headline headline--second">OFFICE</span>
    </h1>
    <p class="subtitle">(Less Noise, More Focus Each Day)</p>
  </main>
</body>
</html>
```